Apartment Investor Business Card Design

Need a new business card designed for my multifamily investment company

Industry/Entity Type

Real Estate

Contact Information for Business Card

Garrick Pelham - President & CEO
Brightwold Holdings, LLC
4838 North 92nd Avenue, Ste 500
Omaha, NE 68999
(402) 555-0147
Garrick@brightwoldholdings.example
Www.BrightwoldHoldings.example

Colors
3176b5

```html
<!DOCTYPE html>
<html lang="en">
<head>
<meta charset="utf-8">
<title>Brightwold Holdings – Business Card</title>
<link rel="stylesheet" href="https://fonts.googleapis.com/css2?family=Cinzel:wght@400;700&family=Tinos&display=swap">
<style>
  :root {
    --backdrop: #1d1d1d;
    --card: #141414;
    --white: #f4f4f4;
    --grey: #bdbdbd;
    --blue: #3176b5;
    --blue-light: #5b8fd0;
  }
  * { margin: 0; padding: 0; box-sizing: border-box; }
  html, body { width: 1200px; height: 1200px; overflow: hidden; background: var(--backdrop); }
  .canvas { position: relative; width: 1200px; height: 1200px; }
  .card {
    position: absolute;
    left: 180px;
    width: 840px;
    height: 480px;
    background: var(--card);
    border-radius: 22px;
  }
  .card--front { top: 90px; }
  .card--back { top: 630px; }

  .brand {
    position: absolute;
    display: flex;
    align-items: center;
    gap: 14px;
    font-family: "Cinzel", serif;
    font-weight: 400;
    color: var(--white);
    white-space: nowrap;
  }
  .brand__dot { width: 14px; height: 14px; border-radius: 50%; background: var(--blue-light); flex: none; }
  .card--front .brand { top: 190px; left: 50%; transform: translateX(-50%); font-size: 42px; letter-spacing: 2px; }
  .front__url {
    position: absolute; top: 340px; width: 100%; text-align: center;
    font-family: "Cinzel", serif; font-size: 14px; letter-spacing: 1.5px; color: var(--grey);
  }

  .holder { position: absolute; top: 60px; left: 70px; font-family: "Cinzel", serif; }
  .holder__name { font-size: 28px; font-weight: 700; color: var(--white); letter-spacing: 1px; }
  .holder__title { font-size: 20px; font-weight: 700; color: var(--blue-light); letter-spacing: 1px; margin-top: -2px; }

  .contact { position: absolute; top: 240px; left: 70px; font-family: "Tinos", serif; font-size: 20px; color: var(--white); line-height: 1.3; }
  .contact__address { margin-bottom: 12px; padding-left: 30px; }
  .contact__row { display: flex; align-items: center; gap: 14px; margin-bottom: 4px; }
  .contact__row svg { width: 18px; height: 18px; flex: none; }

  .card--back .brand { top: 200px; right: 50px; font-size: 24px; letter-spacing: 1px; gap: 10px; }
  .card--back .brand__dot { width: 11px; height: 11px; }
</style>
</head>
<body>
<main class="canvas">
  <section class="card card--front">
    <div class="brand"><span class="brand__dot"></span>Brightwold Holdings</div>
    <p class="front__url">WWW.BRIGHTWOLDHOLDINGS.EXAMPLE</p>
  </section>

  <section class="card card--back">
    <header class="holder">
      <h1 class="holder__name">GARRICK PELHAM</h1>
      <p class="holder__title">PRESIDENT &amp; CEO</p>
    </header>

    <div class="contact">
      <p class="contact__address">4838 North 92nd Avenue, Ste 500<br>Omaha, NE 68999</p>
      <p class="contact__row">
        <svg viewBox="0 0 24 24" aria-hidden="true"><path fill="#5b8fd0" d="M6.6 10.8a15.1 15.1 0 0 0 6.6 6.6l2.2-2.2a1 1 0 0 1 1-.25 11.4 11.4 0 0 0 3.6.57 1 1 0 0 1 1 1V20a1 1 0 0 1-1 1A17 17 0 0 1 3 4a1 1 0 0 1 1-1h3.5a1 1 0 0 1 1 1c0 1.25.2 2.45.57 3.6a1 1 0 0 1-.25 1z"/></svg>
        (402) 555-0147
      </p>
      <p class="contact__row">
        <svg viewBox="0 0 24 24" aria-hidden="true"><rect x="2" y="5" width="20" height="14" fill="none" stroke="#5b8fd0" stroke-width="2"/><path d="M2 5l10 8 10-8" fill="none" stroke="#5b8fd0" stroke-width="2"/></svg>
        Garrick@brightwoldholdings.example
      </p>
      <p class="contact__row">
        <svg viewBox="0 0 24 24" aria-hidden="true"><g fill="none" stroke="#5b8fd0" stroke-width="1.6"><circle cx="12" cy="12" r="10"/><ellipse cx="12" cy="12" rx="4.5" ry="10"/><path d="M2 12h20M4 7h16M4 17h16"/></g></svg>
        Www.BrightwoldHoldings.example
      </p>
    </div>

    <div class="brand"><span class="brand__dot"></span>Brightwold Holdings</div>
  </section>
</main>
</body>
</html>
```